Offer banner redesign / Simplifying existing banner

We have a banner there customer can click on to get an offer. We want to simplify this banner and to get it to at minimum. We are not clear about how it shoulderstand look like, but the actual banner you can see here (It's at the top of the page): https://ofenrohr-lagerhaus.de/kaminsysteme/ We want to get rid of the icons and to reduce the size of the baner. The baner shoulderstand contain the Following text: Affordable chimney using installation service button text: Request free quote

Target Market(s)

Customers from age of 40yrs.

Requirements
Must have
• Clear and good visible button
Nice to have
• It Should be simple and striking.

```html
<!DOCTYPE html>
<html lang="de">
<head>
<meta charset="utf-8">
<title>Angebotsbanner – Ofenrohr Lagerhaus</title>
<link rel="stylesheet" href="https://fonts.googleapis.com/css2?family=Outfit:wght@600&family=Lato:wght@400;700&family=Oswald:wght@400&display=swap">
<style>
  :root {
    --page-bg: #f1f1f1;
    --yellow: #fdbd22;
    --yellow-deep: #fbb03b;
    --dark: #2a2a2a;
    --dark-soft: #3a3a3a;
    --light: #f4f4f4;
    --light-shade: #dcdcdc;
    --ink: #222222;
    --white: #ffffff;
  }
  * { margin: 0; padding: 0; box-sizing: border-box; }
  html, body {
    width: 1200px;
    height: 1200px;
    overflow: hidden;
    background: var(--page-bg);
  }
  .offer-banner {
    position: absolute;
    left: 106px;
    top: 479px;
    width: 1152px;
    height: 309px;
    transform: scale(0.8576);
    transform-origin: top left;
    overflow: hidden;
  }
  .offer-banner__shapes {
    position: absolute;
    inset: 0;
  }
  .headline {
    position: absolute;
    left: 80px;
    top: 78px;
    font-family: "Outfit", sans-serif;
    font-weight: 600;
    font-size: 64px;
    line-height: 62px;
    letter-spacing: 3.6px;
  }
  .headline__top { display: block; color: var(--ink); }
  .headline__bottom { display: block; color: var(--white); }
  .headline-rule {
    position: absolute;
    left: 84px;
    top: 211px;
    width: 379px;
    height: 3px;
    background: var(--ink);
  }
  .subline {
    position: absolute;
    left: 83px;
    top: 228px;
    font-family: "Lato", sans-serif;
    font-weight: 700;
    font-size: 26px;
    letter-spacing: 0.6px;
    color: var(--ink);
    white-space: nowrap;
  }
  .brand {
    position: absolute;
    left: 600px;
    top: 68px;
    display: flex;
    align-items: center;
    gap: 16px;
  }
  .brand__mark {
    width: 82px;
    height: 82px;
    border-radius: 50%;
    border: 4px solid var(--yellow-deep);
  }
  .brand__name {
    font-family: "Lato", sans-serif;
    font-weight: 400;
    font-size: 40px;
    line-height: 42px;
    color: var(--dark-soft);
    letter-spacing: 2px;
  }
  .cta {
    position: absolute;
    left: 659px;
    top: 189px;
    width: 383px;
    height: 74px;
    border-radius: 37px;
    border: 2px solid var(--dark);
    background: linear-gradient(180deg, #fdc73a 0%, var(--yellow-deep) 100%);
    display: flex;
    align-items: center;
    justify-content: center;
    font-family: "Oswald", sans-serif;
    font-weight: 400;
    font-size: 29px;
    color: var(--ink);
    cursor: pointer;
    white-space: nowrap;
  }
  .cta-shadow {
    position: absolute;
    left: 700px;
    top: 266px;
    width: 300px;
    height: 12px;
    border-radius: 50%;
    background: radial-gradient(ellipse at center, rgba(0,0,0,0.45) 0%, rgba(0,0,0,0) 70%);
  }
</style>
</head>
<body>
  <section class="offer-banner" aria-label="Angebotsbanner">
    <svg class="offer-banner__shapes" viewBox="0 0 1152 309" width="1152" height="309" aria-hidden="true">
      <defs>
        <linearGradient id="light-field" x1="0" y1="0" x2="0" y2="1">
          <stop offset="0" stop-color="#dcdcdc"/>
          <stop offset="0.5" stop-color="#f4f4f4"/>
          <stop offset="1" stop-color="#dcdcdc"/>
        </linearGradient>
        <linearGradient id="yellow-field" x1="0" y1="0" x2="0" y2="1">
          <stop offset="0" stop-color="#fdbf20"/>
          <stop offset="1" stop-color="#fbb33c"/>
        </linearGradient>
        <linearGradient id="dark-field" x1="0" y1="0" x2="0" y2="1">
          <stop offset="0" stop-color="#222"/>
          <stop offset="1" stop-color="#444"/>
        </linearGradient>
      </defs>
      <rect class="field-light" width="1152" height="309" fill="url(#light-field)"/>
      <polygon class="corner-dark" points="0,0 98,0 0,155" fill="url(#dark-field)"/>
      <polygon class="corner-gap" points="98,0 118,0 0,186 0,155" fill="#ffffff"/>
      <polygon class="field-yellow" points="118,0 438,0 633,309 0,309 0,186" fill="url(#yellow-field)"/>
      <polygon class="stripe-dark" points="438,0 472,0 667,309 633,309" fill="#2a2a2a"/>
      <polygon class="stripe-yellow" points="958,0 975,0 1152,282 1152,309" fill="#fdbd22"/>
      <polygon class="corner-dark-right" points="975,0 1152,0 1152,282" fill="url(#dark-field)"/>
    </svg>

    <h1 class="headline">
      <span class="headline__top">Preiswerter</span>
      <span class="headline__bottom">Schornstein</span>
    </h1>
    <div class="headline-rule"></div>
    <p class="subline">Wahlweise mit Montageservice</p>

    <div class="brand">
      <span class="brand__mark"></span>
      <span class="brand__name">OFENROHR<br>LAGERHAUS</span>
    </div>

    <div class="cta-shadow"></div>
    <button class="cta" type="button">kostenloses Angebot anfordern</button>
  </section>
</body>
</html>
```